Luxury Skincare Product Box Packaging Design

Vorastelle is a range of skincare products that help protect, nourish, and strengthen even the most sensitive skin, ensuring it is healthy, glowing, calm, and soft. Skincare practices support skin to enhance its appearance and relieve skin conditions. Your skin reflects your health. It is your body canvas and is an asset. The products contain naturally derived ingredients, aromatherapy oils, sustainable and ethical ingredients, organic ingredients where possible, natural preservatives and Australian oils, fruits, and extracts.

Vorastelle
Tagline is "Where Calm Finds Bloom"

Our products do not contain sulphates, parabens, phthalates, petrochemicals, synthetic colours, nor synthetic fragrances.

Everything about the Vorastelle Skincare name is creative and communicates luxury. Vorastelle from your first glance of the name, you will know that this is a company with excellent products.

By keeping it simple, unique, and elegant is often associated with high quality and is a way to establish trust. Vorastelle is a product that is “pure” and natural, so Vorastelle packaging would look simple, elegant, and clean.

I have uploaded the actual logo design and individual labels for the current skincare range I currently with the ingredients included so you can get an understanding of what I like. I have also added samples of package designs I quite like to assist with your designs.

Each Product box packaging sizes are as follows:

Product One - Exfoliating Herbs: 110mm (H) x 33mm Diameter
Product Two - Probiotic Lotion: 138mm (H) x 33mm Diameter
Product Three - Vitamin A Serum: 120mm (H) x 30mm Diameter
Updates

The Measurements are as follows: Product One: 110mm (H) x 33mm Diameter Product Two: 138mm (H) x 33mm Diameter Product Three: 120mm (H) x 30mm Diameter

Target Market(s)

Women

Requirements
Must have
• Logo, Product Name and ingredients and if you can barcode on the packaging that is the box design I am after
Nice to have
• samples of designs I like but open to suggestions

```html
<!DOCTYPE html>
<html lang="en">
<head>
<meta charset="utf-8">
<title>Vorastelle – Soft Botanical Polish box net</title>
<link rel="stylesheet" href="https://fonts.googleapis.com/css2?family=Playfair+Display:wght@400;700&family=Lato:wght@400&family=Montserrat:wght@400&display=swap">
<style>
  :root {
    --page: #f1f0ee;
    --paper: #ffffff;
    --mint: #bcdccb;
    --copper-dark: #9a6a52;
    --cut: #d2143a;
    --fold: #1fb5ea;
    --ink: #1d1d1b;
    --logo: #c08e77;
  }
  html, body {
    margin: 0;
    padding: 0;
    width: 761px;
    height: 1200px;
    overflow: hidden;
    background: var(--page);
  }
  .box-net { display: block; width: 761px; height: 1200px; }
  .tagline { font-family: "Montserrat", sans-serif; font-size: 15px; letter-spacing: 4.5px; fill: var(--ink); }
  .web { font-family: "Lato", sans-serif; font-size: 12px; fill: #3a2a22; }
  .band-label { font-family: "Lato", sans-serif; font-size: 15px; fill: var(--ink); }
  .volume { font-family: "Lato", sans-serif; font-size: 15px; fill: var(--ink); }
  .product-name { font-family: "Playfair Display", serif; font-weight: 700; font-size: 22px; fill: var(--ink); }
  .brand-name { font-family: "Playfair Display", serif; font-size: 56px; fill: var(--logo); }
  .back-title { font-family: "Playfair Display", serif; font-weight: 700; font-size: 15px; fill: var(--ink); }
  .back-copy { font-family: "Lato", sans-serif; font-size: 11.5px; fill: var(--ink); }
  .icon-label { font-family: "Lato", sans-serif; font-size: 8px; fill: #333; }
  .icon-line { fill: none; stroke: var(--copper-dark); stroke-width: 1.2; }
  .cut-line { fill: none; stroke: var(--cut); stroke-width: 2.6; stroke-linejoin: round; }
  .fold-line { fill: none; stroke: var(--fold); stroke-width: 2; stroke-dasharray: 9 6; }
  .care-frame { fill: none; stroke: var(--ink); stroke-width: 1.4; stroke-dasharray: 4 3; }
</style>
</head>
<body>
<svg class="box-net" viewBox="250 902 1025 1616" xmlns="http://www.w3.org/2000/svg">
  <defs>
    <linearGradient id="copper-band" x1="0" x2="1" y1="0" y2="0">
      <stop offset="0" stop-color="#8d5f48"/>
      <stop offset="0.3" stop-color="#dcab92"/>
      <stop offset="0.5" stop-color="#a8765c"/>
      <stop offset="0.8" stop-color="#e2b39b"/>
      <stop offset="1" stop-color="#9a6a52"/>
    </linearGradient>
    <linearGradient id="blossom-tone" x1="0" x2="1" y1="0" y2="1">
      <stop offset="0" stop-color="#5a9a52"/>
      <stop offset="0.45" stop-color="#f4f4ef"/>
      <stop offset="0.7" stop-color="#f1e4a4"/>
      <stop offset="1" stop-color="#4a8a48"/>
    </linearGradient>
    <clipPath id="net-shape">
      <path id="net-outline" d="M278 1405 L300 1385 L300 1280 L420 1280 Q432 1280 436 1292 L468 1405 L716 1405 L755 1292 Q759 1280 771 1280 L885 1280 L885 1385 L907 1405 L907 1190 C907 1120 960 1098 1031 1098 C1102 1098 1155 1120 1155 1190 L1155 1405 L1245 1420 L1245 2020 L1155 2035 L1155 2040 L907 2040 L870 2150 Q866 2160 855 2160 L740 2160 L740 2060 L716 2040 L716 2220 C716 2300 670 2345 592 2345 C514 2345 468 2300 468 2220 L468 2040 L447 2060 L447 2160 L333 2160 Q321 2160 318 2150 L300 2052 L278 2040 Z"/>
    </clipPath>
  </defs>

  <use href="#net-outline" fill="var(--paper)" stroke="var(--paper)" stroke-width="18"/>
  <use href="#net-outline" fill="var(--paper)"/>
  <g clip-path="url(#net-shape)">
    <rect class="base-mint" x="278" y="1972" width="877" height="400" fill="var(--mint)"/>
    <rect class="copper-strip" x="278" y="1945" width="877" height="27" fill="url(#copper-band)"/>
  </g>

  <g class="folds">
    <line class="fold-line" x1="278" y1="1405" x2="1155" y2="1405"/>
    <line class="fold-line" x1="278" y1="2037" x2="1155" y2="2037"/>
    <line class="fold-line" x1="468" y1="1405" x2="468" y2="2037"/>
    <line class="fold-line" x1="716" y1="1405" x2="716" y2="2037"/>
    <line class="fold-line" x1="907" y1="1405" x2="907" y2="2037"/>
    <line class="fold-line" x1="1155" y1="1405" x2="1155" y2="2037"/>
    <line class="fold-line" x1="940" y1="1225" x2="1120" y2="1225"/>
    <line class="fold-line" x1="500" y1="2218" x2="683" y2="2218"/>
  </g>

  <use href="#net-outline" class="cut-line"/>
  <path class="cut-line" d="M907 1213 L940 1213 L940 1225 M1120 1225 L1120 1213 L1155 1213"/>
  <path class="cut-line" d="M468 2228 L500 2228 L500 2218 M683 2218 L683 2228 L716 2228"/>

  <g class="side-tagline">
    <text class="tagline" transform="translate(379 1675) rotate(-90)" text-anchor="middle">Where Calm Finds Bloom</text>
    <text class="web" x="375" y="1963" text-anchor="middle">www.vorastelle.com</text>
  </g>

  <g class="front-panel">
    <text class="brand-name" transform="translate(585 1625) rotate(-68)" text-anchor="middle">Vorastelle</text>
    <rect x="440" y="1800" width="98" height="145" rx="30" fill="url(#blossom-tone)" role="img" aria-label="White blossom with green leaves"/>
    <text class="product-name" x="596" y="1856" text-anchor="middle">SOFT</text>
    <text class="product-name" x="596" y="1887" text-anchor="middle">Botanical</text>
    <text class="product-name" x="596" y="1912" text-anchor="middle">Polish</text>
    <text class="band-label" x="594" y="1963" text-anchor="middle">All Skin Types</text>
    <text class="volume" x="594" y="2004" text-anchor="middle">40 ml</text>
  </g>

  <g class="badge-column">
    <circle cx="813" cy="1542" r="10" fill="#e8d3c8" role="img" aria-label="Badge for Australian made"/>
    <text class="icon-label" x="813" y="1568" text-anchor="middle">Australian</text>
    <text class="icon-label" x="813" y="1577" text-anchor="middle">made</text>

    <path class="icon-line" d="M813 1614 C800 1605 800 1594 807 1593 C810 1592 812 1594 813 1597 C814 1594 816 1592 819 1593 C826 1594 826 1605 813 1614 Z"/>
    <text class="icon-label" x="813" y="1626" text-anchor="middle">100%</text>
    <text class="icon-label" x="813" y="1635" text-anchor="middle">Vegan</text>

    <circle cx="813" cy="1665" r="9" fill="#e8d3c8" role="img" aria-label="Badge for cruelty free"/>
    <text class="icon-label" x="813" y="1687" text-anchor="middle">Cruelty</text>
    <text class="icon-label" x="813" y="1696" text-anchor="middle">Free</text>

    <path class="icon-line" d="M813 1709 L824 1729 L802 1729 Z"/>
    <text class="icon-label" x="813" y="1744" text-anchor="middle">Please</text>
    <text class="icon-label" x="813" y="1753" text-anchor="middle">Recycle</text>

    <rect class="icon-line" x="803" y="1773" width="20" height="16" rx="2"/>
    <line class="icon-line" x1="801" y1="1770" x2="825" y2="1770"/>
    <text x="813" y="1785" text-anchor="middle" font-family="Lato, sans-serif" font-size="7" fill="#9a6a52">6M</text>
    <text class="icon-label" x="813" y="1802" text-anchor="middle">6 months</text>
    <text class="icon-label" x="813" y="1811" text-anchor="middle">once open</text>

    <text class="web" x="810" y="1963" text-anchor="middle">www.vorastelle.com</text>
  </g>

  <g class="back-panel" text-anchor="middle">
    <text class="back-title" x="1033" y="1453">Soft Botanical Polish</text>
    <text class="back-copy" x="1033" y="1491">· All Skin Types ·</text>
    <text class="back-copy" x="1033" y="1506">Especially kind to reactive, tired</text>
    <text class="back-copy" x="1033" y="1521">and fragile complexions.</text>
    <text class="back-copy" x="1033" y="1540">• • •</text>
    <text class="back-copy" x="1033" y="1565">DIRECTIONS:</text>
    <text class="back-copy" x="1033" y="1580">Blend a little with your usual gentle</text>
    <text class="back-copy" x="1033" y="1595">cleanser. Work over damp skin for</text>
    <text class="back-copy" x="1033" y="1609">about sixty seconds, then rinse</text>
    <text class="back-copy" x="1033" y="1624">away with water or a soft cloth.</text>
    <text class="back-copy" x="1033" y="1638">Use two times a week.</text>
    <text class="back-copy" x="1033" y="1652">• • •</text>
    <text class="back-copy" x="1033" y="1668">INGREDIENTS:</text>
    <text class="back-copy" x="1033" y="1683">AVENA SATIVA (OAT) FLOUR*,</text>
    <text class="back-copy" x="1033" y="1698">ROSA DAMASCENA (ROSE PETALS)*,</text>
    <text class="back-copy" x="1033" y="1712">LAVANDULA ANGUSTIFOLIA</text>
    <text class="back-copy" x="1033" y="1727">(LAVENDER) FLOWER*, CENTELLA</text>
    <text class="back-copy" x="1033" y="1742">ASIATICA LEAF (GOTU KOLA),</text>
    <text class="back-copy" x="1033" y="1756">ASPALATHUS LINEARIS (ROOIBOS)</text>
    <text class="back-copy" x="1033" y="1771">LEAF, BAMBUSA STEM POWDER,</text>
    <text class="back-copy" x="1033" y="1786">HIBISCUS SABDARIFFA</text>
    <text class="back-copy" x="1033" y="1800">(HIBISCUS FLOWERS)</text>
    <text class="back-copy" x="1033" y="1815">*ORGANIC INGREDIENTS</text>
    <text class="back-copy" x="1033" y="1837">• • •</text>
    <rect class="care-frame" x="922" y="1855" width="216" height="70"/>
    <text class="back-copy" x="1033" y="1873">Keep in a cool, dry place.</text>
    <text class="back-copy" x="1033" y="1887">For external use only.</text>
    <text class="back-copy" x="1033" y="1902">Keep away from the eyes.</text>
    <text class="back-copy" x="1033" y="1917">Stop use if redness appears.</text>
    <text class="volume" x="1033" y="2004">40 ml</text>
  </g>
</svg>
</body>
</html>
```